Need Catering Menu designed - design that we want is attached

Hi,
We need a new catering menu designed for our cafe.
I have attached our coffee menu, we would like it to follow the same kind of layout.
It needs to be A4, and can be double sided.
I have attached a word doc of our catering menu, so this is what needs to be on the catering menu you produce.
Also, our contact details need to be on both sides of the menu:
Visit us instore to discuss catering options, or call 0438 672 914 or email marla@tevrostudio.com.au
I have also attached our new logo which I'd like incorporated into the menu
Target Market(s)
Doctors/Nurses
Hospital staff
University Students
Industry/Entity Type
Catering
Look and feel

```html
<!DOCTYPE html>
<html lang="en">
<head>
<meta charset="utf-8">
<title>Bedside Kitchen — Catering Menu</title>
<link rel="stylesheet" href="https://fonts.googleapis.com/css2?family=Cabin:ital,wght@0,400;0,500;1,400&family=Cutive+Mono&family=Yanone+Kaffeesatz:wght@300;400&display=swap">
<style>
  :root {
    --paper: #f6f0e6;
    --paper-edge: #efe6d8;
    --cocoa: #3d2c2e;
    --ink: #1e1718;
    --rule: #6d6062;
    --cream: #f3ebe0;
    --divider: #b9b0ab;
  }
  * { margin: 0; padding: 0; box-sizing: border-box; }
  html, body { width: 848px; height: 1200px; overflow: hidden; }
  body {
    position: relative;
    background: radial-gradient(ellipse at 50% 40%, var(--paper) 55%, var(--paper-edge) 100%);
    font-family: "Cabin", Arial, sans-serif;
    color: var(--ink);
  }
  .brand {
    position: absolute; left: 0; top: 78px; width: 848px;
    display: flex; align-items: center; justify-content: center; gap: 12px;
  }
  .brand-dot { width: 16px; height: 16px; border-radius: 50%; background: var(--cocoa); }
  .brand-name {
    font-family: "Cabin", Arial, sans-serif; font-weight: 500;
    color: var(--cocoa); font-size: 34px; line-height: 1;
  }
  .brand-rule {
    position: absolute; left: 414px; top: 190px; width: 20px; height: 1.5px; background: var(--cocoa);
  }
  .tagline {
    position: absolute; top: 218px; left: 0; width: 848px; text-align: center;
    font-family: "Cutive Mono", "Courier New", monospace; font-size: 29px; color: var(--ink);
    word-spacing: 2px;
  }
  .section { position: absolute; left: 29px; width: 780px; border: 1.5px solid var(--rule); }
  .section-breakfast { top: 296px; height: 250px; }
  .section-tea { top: 606px; height: 250px; }
  .section-lunch { top: 912px; height: 240px; }
  .ribbon {
    position: absolute; top: -22px; left: 50%; transform: translateX(-50%);
    height: 44px; display: flex; align-items: center; justify-content: center;
  }
  .ribbon svg { position: absolute; inset: 0; width: 100%; height: 100%; }
  .ribbon-label {
    position: relative; font-family: "Yanone Kaffeesatz", "Arial Narrow", sans-serif;
    font-weight: 300; color: var(--cream); font-size: 27px; letter-spacing: 0.5px;
    text-transform: uppercase;
  }
  .ribbon-label small { font-size: 21px; text-transform: none; }
  .col { position: absolute; width: 353px; }
  .col-left { left: 17px; }
  .col-right { left: 415px; width: 351px; }
  .divider { position: absolute; left: 394px; width: 1px; background: var(--divider); }
  .menu-list { list-style: none; }
  .menu-item { display: flex; align-items: baseline; font-size: 18.5px; line-height: 25.6px; }
  .menu-item .leader {
    flex: 1; margin: 0 3px; border-bottom: 2px dotted var(--ink); transform: translateY(-5px);
  }
  .note { width: 330px; font-size: 15px; line-height: 21px; color: #3a3234; margin-top: 18px; }
  .lunch-copy { font-size: 18.5px; line-height: 25.6px; }
  .lunch-left { width: 340px; }
  .lunch-right { width: 336px; }
  .lunch-copy em { display: block; font-style: italic; margin-bottom: 4px; }
  .filling { padding-left: 16px; }
  .lunch-copy b { font-weight: 500; }
  .footer {
    position: absolute; top: 1165px; left: 0; width: 848px; text-align: center;
    font-size: 16.5px; color: var(--ink);
  }
</style>
</head>
<body>
  <div class="brand"><span class="brand-dot"></span><span class="brand-name">Bedside Kitchen</span></div>
  <div class="brand-rule"></div>
  <p class="tagline">coffee • catering • food to go</p>

  <section class="section section-breakfast">
    <div class="ribbon" style="width:244px">
      <svg viewBox="0 0 244 44" preserveAspectRatio="none" aria-hidden="true"><polygon points="0,0 244,0 230,22 244,44 0,44 14,22" fill="#3d2c2e"/></svg>
      <span class="ribbon-label">Breakfast</span>
    </div>
    <div class="col col-left" style="top:46px">
      <ul class="menu-list">
        <li class="menu-item">Fruit Platter<span class="leader"></span>$15</li>
        <li class="menu-item">Bacon Egg and Cheese Roll<span class="leader"></span>$6.5</li>
        <li class="menu-item">Vegetarian Brekky Wrap<span class="leader"></span>$6.5</li>
        <li class="menu-item">Ham and Cheese Croissant<span class="leader"></span>$6</li>
        <li class="menu-item">Cheese and Tomato Croissant<span class="leader"></span>$5.5</li>
        <li class="menu-item">Ham and Cheese French Toast<span class="leader"></span>$6.5</li>
        <li class="menu-item">Assorted Yoghurts<span class="leader"></span>$5.5</li>
      </ul>
    </div>
    <div class="divider" style="top:46px;height:182px"></div>
    <div class="col col-right" style="top:46px">
      <ul class="menu-list">
        <li class="menu-item">Bircher Muesli<span class="leader"></span>$5.5</li>
        <li class="menu-item">Chia Pudding<span class="leader"></span>$5.5</li>
        <li class="menu-item">Granola and Yoghurt<span class="leader"></span>$5.5</li>
        <li class="menu-item">Muffin<span class="leader"></span>$4.5</li>
        <li class="menu-item">Mini Muffin<span class="leader"></span>$2.5</li>
        <li class="menu-item">Juice<span class="leader"></span>$8</li>
      </ul>
    </div>
  </section>

  <section class="section section-tea">
    <div class="ribbon" style="width:380px">
      <svg viewBox="0 0 380 44" preserveAspectRatio="none" aria-hidden="true"><polygon points="0,0 380,0 366,22 380,44 0,44 14,22" fill="#3d2c2e"/></svg>
      <span class="ribbon-label">Morning <small>and</small> Afternoon Tea</span>
    </div>
    <div class="col col-left" style="top:44px">
      <ul class="menu-list">
        <li class="menu-item">Fruit Platter<span class="leader"></span>$15</li>
        <li class="menu-item">Muffin<span class="leader"></span>$4.5</li>
        <li class="menu-item">Mini Muffin<span class="leader"></span>$2.5</li>
        <li class="menu-item">Assorted Slices<span class="leader"></span>$4</li>
        <li class="menu-item">Assorted Cookies from<span class="leader"></span>$3</li>
        <li class="menu-item">Assorted Yoghurts<span class="leader"></span>$5.5</li>
        <li class="menu-item">Chia Pudding<span class="leader"></span>$5.5</li>
      </ul>
    </div>
    <div class="divider" style="top:44px;height:182px"></div>
    <div class="col col-right" style="top:44px">
      <ul class="menu-list">
        <li class="menu-item">Banana Bread<span class="leader"></span>$4.5</li>
        <li class="menu-item">Juice<span class="leader"></span>$8</li>
      </ul>
      <p class="note">*Cups/Plates/Serviettes can be provided at a charge of $1 per person</p>
      <p class="note" style="margin-top:20px">*Barista made coffee available</p>
    </div>
  </section>

  <section class="section section-lunch">
    <div class="ribbon" style="width:244px">
      <svg viewBox="0 0 244 44" preserveAspectRatio="none" aria-hidden="true"><polygon points="0,0 244,0 230,22 244,44 0,44 14,22" fill="#3d2c2e"/></svg>
      <span class="ribbon-label">Lunch</span>
    </div>
    <div class="col col-left lunch-copy lunch-left" style="top:38px">
      <div class="menu-item" style="width:297px">Sandwiches&nbsp; or Wraps<span class="leader"></span>$7.50</div>
      <em>Sandwiches cut into quarters – Wraps cut into thirds</em>
      <p class="filling">•<b>Ham</b>: butter, pickle spread, cheese, tomato, champagne leg ham</p>
      <p class="filling">•<b>Turkey</b>: butter, cranberry sauce, lettuce mix, tomato, turkey breast</p>
    </div>
    <div class="divider" style="top:38px;height:180px"></div>
    <div class="col col-right lunch-copy lunch-right" style="top:38px">
      <p>•<b>Sweet Chilli Chicken</b>:&nbsp; butter, sweet chilli sauce, aioli, lettuce mix, tomato, cheese, sweet chilli chicken tenders</p>
      <p>•<b>Chicken Schnitzel</b>: butter, aioli, lettuce mix, tomato, tasty cheese, chicken schnitzel</p>
    </div>
  </section>

  <p class="footer">Visit us instore to discuss catering options, or call 0438 672 914 or email marla@tevrostudio.com.au</p>
</body>
</html>
```